Lorn & Vell Designs - Promotions flyer

I am a locally based Interior designer /stylist on Sydney's lower north shore. I would like to offer my services:
Full Professional Styling Services and Furniture Hire
Colour Consultation – Interior / exterior
Floor Coverings
Furniture selection and sourcing
Window Treatments
Wallpaper
Soft Furnishings
Upholstery
Renovations

I would like to offer a free consultation
Updates

Project Deadline Extended
Reason: I've been speaking with a designer and need her to make one more change. I have tried to message her twice, but have had no reply. Once she makes these changes I'm ready to sign off on the design. Thanks Harriet

Target Market(s)

30 - 60's middle to high income earners

Industry/Entity Type

Floor

Requirements
Must have
• one sided DL size
Use my logo
1 or 2 images of interior space or image of a lamp, cushion, lounge etc
The following contact details:
Mobile: 041 xxx xxxx
Website Address: www.lornandvelldesigns.example.au

```html
<!DOCTYPE html>
<html lang="en">
<head>
<meta charset="utf-8">
<title>Lorn &amp; Vell Designs – Promotions Flyer</title>
<link rel="stylesheet" href="https://fonts.googleapis.com/css2?family=Jost:wght@300;400;600;700&family=Oswald:wght@300;400;600&display=swap">
<style>
  :root {
    --backdrop: #3b302a;
    --cream: #ebe8df;
    --orange: #f26a21;
    --ink: #111111;
    --photo-light: #e4e6ea;
    --photo-mid: #b3b7bf;
    --photo-dark: #5b6172;
    --white: #ffffff;
  }
  html, body {
    margin: 0;
    width: 1200px;
    height: 685px;
    overflow: hidden;
    background: var(--backdrop);
  }
  .flyer {
    position: absolute;
    left: 40px;
    top: 76px;
    width: 1120px;
    height: 533px;
    background: var(--cream);
    overflow: hidden;
    font-family: "Jost", sans-serif;
    color: var(--ink);
  }
  .hero-photo {
    position: absolute;
    left: 0;
    top: 0;
    width: 760px;
    height: 461px;
    background:
      radial-gradient(ellipse 40% 30% at 45% 70%, var(--photo-dark), transparent 70%),
      radial-gradient(ellipse 30% 40% at 75% 25%, var(--photo-light), transparent 70%),
      linear-gradient(180deg, var(--photo-light) 0%, var(--photo-mid) 55%, var(--photo-dark) 100%);
    -webkit-mask-image: linear-gradient(90deg, #000 78%, transparent 100%);
    mask-image: linear-gradient(90deg, #000 78%, transparent 100%);
  }
  .brand-name {
    position: absolute;
    left: 56px;
    top: 60px;
    display: flex;
    align-items: center;
    gap: 14px;
    font-weight: 400;
    font-size: 46px;
    line-height: 1;
    color: var(--ink);
  }
  .brand-name::before {
    content: "";
    width: 22px;
    height: 22px;
    background: var(--orange);
  }
  .offer-seal {
    position: absolute;
    left: 30px;
    top: 345px;
    width: 158px;
    height: 158px;
    z-index: 2;
  }
  .tagline {
    margin: 0;
    font-size: inherit;
  }
  .tagline span {
    position: absolute;
    line-height: 1;
    white-space: nowrap;
  }
  .line-we    { left: 843px; top: 42px;  font-weight: 300; font-size: 44px; }
  .line-space { left: 813px; top: 76px;  font-weight: 700; font-size: 62px; letter-spacing: -0.5px; }
  .line-and   { left: 1000px; top: 116px; font-weight: 300; font-size: 20px; }
  .line-make  { left: 872px; top: 133px; font-weight: 300; font-size: 44px; }
  .line-your  { left: 843px; top: 166px; font-weight: 300; font-size: 42px; }
  .line-place { left: 768px; top: 181px; font-weight: 700; font-size: 76px; letter-spacing: -0.5px; }
  .services {
    position: absolute;
    left: 675px;
    top: 292px;
    width: 440px;
    text-align: center;
    font-family: "Oswald", sans-serif;
  }
  .services-heading {
    margin: 0 0 4px;
    font-weight: 600;
    font-size: 27px;
    line-height: 1.13;
  }
  .services-list {
    margin: 0;
    font-weight: 300;
    font-size: 20px;
    line-height: 26px;
    letter-spacing: -0.2px;
  }
  .dot {
    display: inline-block;
    width: 13px;
    height: 13px;
    border-radius: 50%;
    background: var(--orange);
    margin: 0 1px;
    vertical-align: -1px;
  }
  .contact-band {
    position: absolute;
    left: 0;
    bottom: 0;
    width: 100%;
    height: 73px;
    background: var(--orange);
  }
  .contact-band span {
    position: absolute;
    top: 0;
    height: 73px;
    display: flex;
    align-items: center;
    white-space: nowrap;
  }
  .contact-mobile {
    left: 330px;
    font-weight: 600;
    font-size: 27px;
  }
  .contact-web {
    left: 681px;
    font-weight: 400;
    font-size: 24px;
  }
</style>
</head>
<body>
  <main class="flyer">
    <div class="hero-photo" role="img" aria-label="Photo of a styled bedroom with silver tufted cushions, grey bedding, a white carved headboard and a silver table lamp"></div>

    <div class="brand-name">Lorn &amp; Vell</div>

    <svg class="offer-seal" viewBox="0 0 158 158" role="img" aria-label="Free consultation">
      <defs>
        <path id="seal-top" d="M 27 79 A 52 52 0 0 1 131 79"/>
        <path id="seal-bottom" d="M 16 79 A 63 63 0 0 0 142 79"/>
      </defs>
      <circle cx="79" cy="79" r="77" fill="var(--white)"/>
      <circle cx="79" cy="79" r="70" fill="var(--orange)"/>
      <circle cx="79" cy="79" r="40" fill="var(--cream)" stroke="var(--white)" stroke-width="3"/>
      <text font-family="Jost, sans-serif" font-weight="600" font-size="15" fill="var(--white)" text-anchor="middle" letter-spacing="1">
        <textPath href="#seal-top" startOffset="50%">FREE</textPath>
      </text>
      <text font-family="Jost, sans-serif" font-weight="600" font-size="13" fill="var(--white)" text-anchor="middle" letter-spacing="1">
        <textPath href="#seal-bottom" startOffset="50%">CONSULTATION</textPath>
      </text>
    </svg>

    <h1 class="tagline" aria-label="We Take Space and Make It Your Place!">
      <span class="line-we">We Take</span>
      <span class="line-space">Space</span>
      <span class="line-and">and</span>
      <span class="line-make">Make It</span>
      <span class="line-your">Your</span>
      <span class="line-place">Place!</span>
    </h1>

    <section class="services">
      <h2 class="services-heading">Full Professional Styling<br>Services and Furniture Hire</h2>
      <p class="services-list">
        Colour Consultation – Interior/exterior <span class="dot"></span> Floor Coverings<br>
        Furniture selection and sourcing <span class="dot"></span> Window Treatments<br>
        Wallpaper <span class="dot"></span> Soft Furnishings <span class="dot"></span> Upholstery <span class="dot"></span> Renovations
      </p>
    </section>

    <footer class="contact-band">
      <span class="contact-mobile">Mobile: 041 xxx xxxx</span>
      <span class="contact-web">www.lornandvelldesigns.example.au</span>
    </footer>
  </main>
</body>
</html>
```